Willow of Meadow Uniform Label Redesign

To refine our current product label designs into one, simple, modern, crisp, general look that can be adapted to all our all Natural Skin Care and Wellness products. I am inspired by the elegant versatility of products like Lumavel Botanic Beauty or Tarn Beauty label schemes. We no longer want labels that indicate scent or ingredients. We have two primary colors that we want to maintain (#096CA3 and #DEE33F), and are willing to entertain subtle additions of others, other than black. Our labels will be printed on white or clear material. We use mainly Cosmo or Boston Round container shapes, plus flat top, smooth, round jars. Maybe a faded watermark highlight the "natural" or "beautiful" side of our products. we need to convey confidence, while remaining simple. We currently use the Advantage font. Maybe Century Gothic may work. Something similar that is easy on the eyes. Maybe vertical main text? We are willing to entertain a lot of ideas. These designs will offer ideas into our eventual Website (www.willowofmeadow-example.com) redesign.

Target Market(s)

Those who are familiar with the power of natural, plant based skin care and wellness products

Industry/Entity Type

Natural Skin Care and Wellness

Font styles to use
Sans Serif
Other font styles liked:
• Century Gothic, Advantage, or similar that is easy on the eyes

Colors
0054AA
0677BA
7BADD7
CADEEF
E8F1F8
59FF00
82FF00
B8FF75
E3FFCB
F4FFEA

Requirements
Must have
• "Clean Lines"; These colors: (#096CA3 and #DEE33F)
Nice to have
• MAYBE vertical main text or a watermark image

```html
<!DOCTYPE html>
<html lang="en">
<head>
<meta charset="utf-8">
<title>Willow of Meadow – Label System</title>
<link rel="stylesheet" href="https://fonts.googleapis.com/css2?family=Asap:ital,wght@0,400;0,600;0,700;1,400&family=Lato:wght@400;700;900&family=Montserrat:wght@500&display=swap">
<style>
  :root {
    --brand-blue: #096ca3;
    --brand-lime: #dee33f;
    --band-green: #e3ffcb;
    --label-white: #fcfcfc;
    --ink: #2b2b2b;
    --stage: #ffffff;
    --watermark: rgba(255, 255, 255, 0.6);
  }
  * { box-sizing: border-box; margin: 0; padding: 0; }
  html, body {
    width: 1200px;
    height: 886px;
    overflow: hidden;
    background: var(--stage);
  }
  .sheet {
    position: relative;
    width: 1200px;
    height: 886px;
    display: flex;
    flex-direction: column;
    align-items: center;
    justify-content: center;
    gap: 30px;
  }
  .label {
    position: relative;
    width: 800px;
    height: 400px;
    background: var(--label-white);
    overflow: hidden;
    font-family: "Lato", sans-serif;
    color: var(--ink);
    box-shadow: 0 0 0 1px #e4e4e4;
  }
  .label__band {
    position: absolute;
    left: 0; right: 0; top: 180px; bottom: 0;
    background: var(--band-green);
  }
  .label__watermark {
    position: absolute;
    left: 22px;
    top: 300px;
    font-family: "Montserrat", sans-serif;
    font-weight: 500;
    font-size: 132px;
    line-height: 1;
    letter-spacing: 22px;
    color: var(--watermark);
    white-space: nowrap;
  }
  .label__ingredients {
    position: absolute;
    left: 32px; top: 24px;
    font-size: 14px;
    line-height: 17.6px;
  }
  .label__usage {
    position: absolute;
    right: 17px; top: 30px;
    font-size: 14px;
    line-height: 17.6px;
    text-align: right;
  }
  .section-title { margin-bottom: 17px; }
  .usage-block + .usage-block { margin-top: 17px; }
  .label__mark {
    position: absolute;
    left: 437px; top: 30px;
    transform: translateX(-50%);
    display: flex;
    align-items: center;
    gap: 8px;
    font-family: "Asap", sans-serif;
    font-weight: 600;
    font-size: 14px;
    color: var(--brand-blue);
    white-space: nowrap;
  }
  .label__mark-dot {
    width: 44px; height: 44px;
    border: 3px solid var(--brand-lime);
    border-radius: 50%;
  }
  .label__center {
    position: absolute;
    left: 437px; top: 166px;
    transform: translateX(-50%);
    text-align: center;
    white-space: nowrap;
  }
  .brand-name {
    font-family: "Asap", sans-serif;
    font-weight: 700;
    font-size: 22px;
    color: var(--brand-blue);
    letter-spacing: 0.3px;
  }
  .product-name {
    margin-top: 26px;
    font-family: "Asap", sans-serif;
    font-weight: 700;
    font-size: 23px;
    letter-spacing: 0.5px;
  }
  .product-name--large { font-size: 27px; }
  .product-variant {
    margin-top: 6px;
    font-size: 16px;
    letter-spacing: 0.3px;
  }
  .label__note {
    position: absolute;
    left: 24px; top: 223px;
    width: 197px; height: 75px;
    border: 1.5px solid var(--brand-blue);
    padding: 7px 6px;
    font-weight: 900;
    font-size: 14px;
    line-height: 17.5px;
  }
  .label__tagline {
    position: absolute;
    left: 437px; top: 348px;
    transform: translateX(-50%);
    width: 198px; height: 30px;
    border: 1.5px solid var(--brand-blue);
    display: flex; align-items: center; justify-content: center;
    font-family: "Asap", sans-serif;
    font-style: italic;
    font-size: 14px;
    letter-spacing: 0.4px;
    color: var(--brand-blue);
  }
</style>
</head>
<body>
<main class="sheet">

  <article class="label label--lotion">
    <div class="label__band"></div>
    <div class="label__watermark" aria-hidden="true">NATURAL</div>

    <section class="label__ingredients">
      <p class="section-title">Ingredients :</p>
      <p>This test is just for copy use.<br>this test is just for copy use.<br>this test is just for cop y use.<br>this test is just for copy use.<br>this test is just for copy use.<br>this test is just for copy use.</p>
    </section>

    <div class="label__mark"><span class="label__mark-dot"></span></div>

    <div class="label__center">
      <p class="brand-name">WILLOW OF MEADOW</p>
      <h2 class="product-name">HYDRATING LOTION</h2>
      <p class="product-variant">ALOE AND SHEA</p>
    </div>

    <section class="label__usage">
      <p class="section-title">How to Use</p>
      <p class="usage-block">This test is just for copy use.<br>this test is just for copy use.<br>this test is just for cop y use.<br>this test is just for copy use.<br>this test is just for copy use.<br>this test is just for copy use.</p>
      <p class="usage-block">This test is just for copy use.<br>this test is just for copy use.<br>this test is just for cop y use.<br>this test is just for copy use.<br>this test is just for copy use.<br>this test is just for copy use.</p>
    </section>

    <p class="label__note">this test is just for copy use. this test is just for copy use.</p>
    <p class="label__tagline">Simple. Beautiful. Timeless</p>
  </article>

  <article class="label label--polish">
    <div class="label__band"></div>
    <div class="label__watermark" aria-hidden="true">NATURAL</div>

    <section class="label__ingredients">
      <p class="section-title">Ingredients :</p>
      <p>This test is just for copy use.<br>this test is just for copy use.<br>this test is just for cop y use.<br>this test is just for copy use.<br>this test is just for copy use.<br>this test is just for copy use.</p>
    </section>

    <div class="label__mark"><span class="label__mark-dot"></span></div>

    <div class="label__center">
      <p class="brand-name">WILLOW OF MEADOW</p>
      <h2 class="product-name product-name--large">BODY POLISH</h2>
      <p class="product-variant">SHEA AND SUGAR | ROSE GERANIUM</p>
    </div>

    <section class="label__usage">
      <p class="section-title">How to Use</p>
      <p class="usage-block">This test is just for copy use.<br>this test is just for copy use.<br>this test is just for cop y use.<br>this test is just for copy use.<br>this test is just for copy use.<br>this test is just for copy use.</p>
      <p class="usage-block">This test is just for copy use.<br>this test is just for copy use.<br>this test is just for cop y use.<br>this test is just for copy use.<br>this test is just for copy use.<br>this test is just for copy use.</p>
    </section>

    <p class="label__note">this test is just for copy use. this test is just for copy use.</p>
    <p class="label__tagline">Simple. Beautiful. Timeless</p>
  </article>

</main>
</body>
</html>
```